Letterhead in Word Format

We are a small law firm in the Midwest. Our clientele is generally small business owners and companies.

We recently had a complete re-brand with a new logo, new letterhead, business cards, etc. However, the major issue now is that we cannot use the letterhead without physically ordering letterhead. Thus, invoices, and other items cannot be custom drafted.

We require custom letterhead in MICROSOFT WORD format. Our logo will be provided to you. And we will also provide a copy of the letterhead that was prepared.

We would like to see designs that are black and white, sophisticated, elegant, and generally professional. We prefer a traditional design with just a touch of contemporary.

Please do not submit any designs that are not Microsoft Word compatible.

EDIT: Please view the attached letterhead. The design must include the logo, name, address, fax, phone, email, and name of attorney.
Updates

Thank you all for submitting designs. I just wanted to quickly provide some feedback. I saw a few designs that had the logo at the bottom. Because there will be text with margins at 1" all around, it's not practical have the logo at the bottom. Also, designs with blocks of gray or black would cause our printer to bleed black onto the letterhead, so that is not practical as well.

If you have any comments, please feel free to leave me a message. Thank you.

Target Market(s)

Small business owners, companies, real estate investors and developers.

Industry/Entity Type

Small Business

Font styles to use
Script

Requirements
Must have
• Microsoft Word Format

```html
<!DOCTYPE html>
<html lang="en">
<head>
<meta charset="utf-8">
<title>The Orland Law Firm – Letterhead</title>
<link rel="stylesheet" href="https://fonts.googleapis.com/css2?family=EB+Garamond:wght@400&display=swap">
<style>
  :root {
    --ink: #0d0d0d;
    --paper: #ffffff;
    --rule: #4a4a4a;
    --rule-light: #9a9a9a;
  }
  * { margin: 0; padding: 0; box-sizing: border-box; }
  html, body { width: 927px; height: 1200px; overflow: hidden; background: var(--paper); }
  .letterhead {
    position: relative;
    width: 927px;
    height: 1200px;
    background: var(--paper);
    font-family: "EB Garamond", Garamond, serif;
    overflow: hidden;
  }
  .header-frame { position: absolute; left: 0; top: 0; width: 927px; height: 140px; }
  .contact {
    position: absolute;
    top: 44px;
    color: var(--ink);
    font-size: 13.5px;
    line-height: 17.5px;
    font-style: normal;
  }
  .contact--left { left: 29px; }
  .contact--right { right: 28px; text-align: right; }
  .firm-name {
    position: absolute;
    left: 0;
    width: 927px;
    top: 110px;
    text-align: center;
    color: var(--ink);
    font-size: 23px;
    font-weight: 400;
    letter-spacing: 0.5px;
  }
  .attorney {
    position: absolute;
    left: 0;
    width: 927px;
    top: 142px;
    text-align: center;
    color: var(--ink);
    font-size: 13.5px;
    letter-spacing: 1px;
  }
</style>
</head>
<body>
  <main class="letterhead">
    <svg class="header-frame" width="927" height="140" viewBox="0 0 927 140" aria-hidden="true">
      <path d="M0 106 H313.5 A153 93 0 0 1 613.5 106 H927" fill="none" stroke="var(--ink)" stroke-width="1.5"/>
      <g class="rule">
        <rect x="0" y="120" width="319" height="9" fill="var(--rule-light)"/>
        <rect x="0" y="121.5" width="319" height="1.5" fill="var(--rule)"/>
        <rect x="0" y="126" width="319" height="1.5" fill="var(--rule)"/>
        <rect x="608" y="120" width="319" height="9" fill="var(--rule-light)"/>
        <rect x="608" y="121.5" width="319" height="1.5" fill="var(--rule)"/>
        <rect x="608" y="126" width="319" height="1.5" fill="var(--rule)"/>
      </g>
    </svg>

    <address class="contact contact--left">
      Phone: (555) 014-2290<br>
      Address: 2417 W. Larkin Ave.<br>
      Fairbrook, Illinois 60999
    </address>

    <address class="contact contact--right">
      Fax: (555) 014-2291<br>
      Web: www.orlandlawfirm.com<br>
      Email: office@orlandlawfirm.com
    </address>

    <h1 class="firm-name">THE ORLAND LAW FIRM</h1>
    <p class="attorney">Margaret L. Orland, Attorney at Law</p>
  </main>
</body>
</html>
```